Korvane Technologies - Business Card & Stationary
"Moving Forward"
Everyone, we are making our decision now. Thank you for your patience.
Wow, you guys are really doing a superb job. We really like a majority of the designs submitted thus far. There is no clear winner yet, so please keep them coming!
A couple things: bluecrest - We like where you are going with #38, #41, & #42. I like the back of the card ideas you have had so far. We like the backs of #41, & #42, but the back of #40 is just too dark.
dorvalstudio - Like #20, #21, & #33. Really like the Grey/Silver logo on the back too.
lumbrafox - #37 is one of our favorites!
We would like to see what some of you guys have in mind for stationary too!
Great job everyone! 1, 3, 5, 6 - we really like the front design, but would like the back side to be more subtle. 10 & 11 are both great. Would like the logo centered on the back of #10 like #7. I am not too keen on the solid green areas like #'s 8 & 9.
This is a project to include business cards and stationary!! I apologize if that wasn't clear.

```html
<!DOCTYPE html>
<html lang="en">
<head>
<meta charset="utf-8">
<title>Korvane Technologies — Business Card &amp; Stationery</title>
<link rel="stylesheet" href="https://fonts.googleapis.com/css2?family=Open+Sans:wght@400;600;700&display=swap">
<style>
  :root {
    --bg: #e4e6e8;
    --paper: #ffffff;
    --blue: #1d4f8f;
    --blue-dark: #123a6b;
    --green: #5fae3c;
    --green-light: #8cc63f;
    --ink: #3d4248;
    --muted: #8a9096;
    --faint: #eef0f2;
    --line: #d5d9dd;
  }
  * { margin: 0; padding: 0; box-sizing: border-box; }
  html, body { width: 1200px; height: 622px; overflow: hidden; }
  body {
    background: var(--bg);
    font-family: "Open Sans", Arial, sans-serif;
    color: var(--ink);
    position: relative;
  }
  .piece {
    position: absolute;
    background: var(--paper);
    box-shadow: 0 2px 6px rgba(0,0,0,.18);
    overflow: hidden;
  }
  .piece > svg.art { position: absolute; inset: 0; width: 100%; height: 100%; }

  .brand {
    position: absolute;
    display: flex;
    align-items: center;
    gap: 5px;
    font-weight: 700;
    color: var(--blue);
    text-transform: uppercase;
    line-height: 1;
  }
  .brand-dot { border-radius: 50%; background: var(--green); flex: none; }
  .brand-name { letter-spacing: .04em; }

  /* business cards */
  .card { width: 200px; height: 115px; }
  .card-front { left: 20px; top: 20px; }
  .card-back { left: 235px; top: 20px; background: linear-gradient(120deg, var(--blue-dark), var(--blue) 55%, var(--green)); }
  .card-front .brand { left: 64px; top: 14px; font-size: 9px; }
  .card-front .brand-dot { width: 10px; height: 10px; }
  .card-contact { position: absolute; left: 64px; top: 42px; font-size: 6px; line-height: 1.5; }
  .card-contact .person { font-size: 7.5px; font-weight: 700; color: var(--blue); }
  .card-contact .role { color: var(--muted); margin-bottom: 4px; }
  .card-back .brand { left: 0; right: 0; top: 44px; justify-content: center; color: #fff; font-size: 11px; }
  .card-back .brand-dot { width: 12px; height: 12px; background: #fff; }
  .card-back .tagline { position: absolute; left: 0; right: 0; top: 64px; text-align: center; color: #dfe9f3; font-size: 6px; letter-spacing: .2em; text-transform: uppercase; }

  /* envelopes */
  .env-flap { left: 20px; top: 155px; width: 415px; height: 200px; }
  .env-flap .brand { left: 0; right: 0; top: 92px; justify-content: center; color: #fff; font-size: 10px; }
  .env-flap .brand-dot { width: 11px; height: 11px; background: #fff; }
  .env { width: 330px; height: 125px; }
  .env-a { left: 20px; top: 380px; width: 415px; height: 200px; }
  .env-b { left: 470px; top: 478px; }
  .env-c { left: 835px; top: 478px; }
  .env .brand { left: 40px; top: 12px; font-size: 9px; }
  .env-a .brand { left: 52px; top: 18px; font-size: 11px; }
  .env .brand-dot { width: 10px; height: 10px; }
  .return-address { position: absolute; left: 40px; top: 26px; font-size: 5.5px; color: var(--muted); }
  .env-a .return-address { left: 52px; top: 36px; font-size: 7px; }
  .window { position: absolute; left: 30px; bottom: 22px; width: 130px; height: 42px; border: 1px solid var(--line); border-radius: 3px; background: var(--faint); }

  /* letterheads */
  .letter { top: 20px; width: 340px; height: 440px; }
  .letter-a { left: 470px; }
  .letter-b { left: 835px; }
  .letter .brand { left: 84px; top: 20px; font-size: 11px; }
  .letter .brand-dot { width: 12px; height: 12px; }
  .letter .tagline { position: absolute; left: 101px; top: 34px; font-size: 5.5px; letter-spacing: .2em; color: var(--muted); text-transform: uppercase; }
  .watermark { position: absolute; right: 40px; top: 170px; width: 150px; height: 150px; border-radius: 50%; background: var(--faint); }
  .letter-body { position: absolute; left: 34px; right: 34px; top: 80px; font-size: 5.5px; line-height: 1.55; }
  .letter-body p { margin-bottom: 7px; }
  .letter-footer { position: absolute; left: 0; right: 0; bottom: 38px; text-align: center; font-size: 5px; color: var(--muted); }
</style>
</head>
<body>
<svg width="0" height="0" style="position:absolute">
  <defs>
    <linearGradient id="blueGrad" x1="0" y1="0" x2="1" y2="1">
      <stop offset="0" stop-color="#123a6b"/><stop offset="1" stop-color="#1d4f8f"/>
    </linearGradient>
    <linearGradient id="greenGrad" x1="0" y1="0" x2="1" y2="0">
      <stop offset="0" stop-color="#5fae3c"/><stop offset="1" stop-color="#8cc63f"/>
    </linearGradient>
    <linearGradient id="bandGrad" x1="0" y1="0" x2="1" y2="0">
      <stop offset="0" stop-color="#123a6b"/><stop offset=".6" stop-color="#1d4f8f"/><stop offset="1" stop-color="#5fae3c"/>
    </linearGradient>
  </defs>
</svg>

<!-- business card front -->
<div class="piece card card-front">
  <svg class="art" viewBox="0 0 200 115" preserveAspectRatio="none" aria-hidden="true">
    <path d="M0 0 H58 C42 40 26 80 0 115 Z" fill="url(#blueGrad)"/>
    <path d="M58 0 H66 C50 42 32 82 6 115 H0 C26 80 42 40 58 0 Z" fill="url(#greenGrad)"/>
  </svg>
  <div class="brand"><span class="brand-dot"></span><span class="brand-name">Korvane Technologies</span></div>
  <div class="card-contact">
    <div class="person">Dana Whitfield</div>
    <div class="role">Project Director</div>
    <div>613 555 0142</div>
    <div>dana@korvanetech.com</div>
    <div>korvanetech.com</div>
  </div>
</div>

<!-- business card back -->
<div class="piece card card-back">
  <svg class="art" viewBox="0 0 200 115" preserveAspectRatio="none" aria-hidden="true">
    <path d="M0 88 C60 70 130 104 200 78 V115 H0 Z" fill="#ffffff" opacity=".12"/>
  </svg>
  <div class="brand"><span class="brand-dot"></span><span class="brand-name">Korvane Technologies</span></div>
  <div class="tagline">Moving Forward</div>
</div>

<!-- envelope, flap side -->
<div class="piece env-flap">
  <svg class="art" viewBox="0 0 415 200" preserveAspectRatio="none" aria-hidden="true">
    <path d="M0 70 C140 50 280 90 415 60 V130 C280 160 140 120 0 140 Z" fill="url(#bandGrad)"/>
    <path d="M0 0 L207 110 L415 0" fill="none" stroke="#d5d9dd" stroke-width="1"/>
  </svg>
  <div class="brand"><span class="brand-dot"></span><span class="brand-name">Korvane Technologies</span></div>
</div>

<!-- envelope, address side -->
<div class="piece env-a">
  <svg class="art" viewBox="0 0 415 200" preserveAspectRatio="none" aria-hidden="true">
    <path d="M0 0 H46 C34 20 20 38 0 52 Z" fill="url(#blueGrad)"/>
    <path d="M0 176 C140 168 280 186 415 166 V200 H0 Z" fill="url(#blueGrad)"/>
    <path d="M0 170 C140 162 280 180 415 160 V166 C280 186 140 168 0 176 Z" fill="url(#greenGrad)"/>
  </svg>
  <div class="brand"><span class="brand-dot"></span><span class="brand-name">Korvane Technologies</span></div>
  <div class="return-address">120 Meridian Way, Suite 4, Ottawa</div>
</div>

<!-- letterhead one -->
<div class="piece letter letter-a">
  <svg class="art" viewBox="0 0 340 440" preserveAspectRatio="none" aria-hidden="true">
    <path d="M0 0 H76 C56 22 32 40 0 58 Z" fill="url(#blueGrad)"/>
    <path d="M76 0 H86 C64 26 36 46 0 66 V58 C32 40 56 22 76 0 Z" fill="url(#greenGrad)"/>
    <path d="M0 418 C110 408 230 426 340 402 V440 H0 Z" fill="url(#blueGrad)"/>
    <path d="M0 410 C110 400 230 418 340 394 V402 C230 426 110 408 0 418 Z" fill="url(#greenGrad)"/>
  </svg>
  <div class="watermark"></div>
  <div class="brand"><span class="brand-dot"></span><span class="brand-name">Korvane Technologies</span></div>
  <div class="tagline">Moving Forward</div>
  <div class="letter-body">
    <p>Dana Whitfield<br>42 Harbor Lane<br>Lakeview, ON 10452</p>
    <p>May 1, 2024</p>
    <p>Dear Ms. Hale,</p>
    <p>Thank you for meeting with our team last week. We are glad to share the next steps for the project and the schedule we agreed upon together.</p>
    <p>Our engineers will begin the first phase this month and report progress every two weeks. Please let us know if anything changes on your side.</p>
    <p>We look forward to working with you.</p>
    <p>Sincerely,<br>Dana Whitfield</p>
  </div>
  <div class="letter-footer">120 Meridian Way, Suite 4 · Ottawa · 613 555 0142 · korvanetech.com</div>
</div>

<!-- letterhead two -->
<div class="piece letter letter-b">
  <svg class="art" viewBox="0 0 340 440" preserveAspectRatio="none" aria-hidden="true">
    <path d="M0 0 H76 C56 22 32 40 0 58 Z" fill="url(#blueGrad)"/>
    <path d="M76 0 H86 C64 26 36 46 0 66 V58 C32 40 56 22 76 0 Z" fill="url(#greenGrad)"/>
    <path d="M0 418 C110 408 230 426 340 402 V440 H0 Z" fill="url(#blueGrad)"/>
    <path d="M0 410 C110 400 230 418 340 394 V402 C230 426 110 408 0 418 Z" fill="url(#greenGrad)"/>
  </svg>
  <div class="watermark"></div>
  <div class="brand"><span class="brand-dot"></span><span class="brand-name">Korvane Technologies</span></div>
  <div class="tagline">Moving Forward</div>
  <div class="letter-body">
    <p>Dana Whitfield<br>42 Harbor Lane<br>Lakeview, ON 10452</p>
    <p>May 1, 2024</p>
    <p>Dear Ms. Hale,</p>
    <p>Thank you for meeting with our team last week. We are glad to share the next steps for the project and the schedule we agreed upon together.</p>
    <p>Our engineers will begin the first phase this month and report progress every two weeks. Please let us know if anything changes on your side.</p>
    <p>We look forward to working with you.</p>
    <p>Sincerely,<br>Dana Whitfield</p>
  </div>
  <div class="letter-footer">120 Meridian Way, Suite 4 · Ottawa · 613 555 0142 · korvanetech.com</div>
</div>

<!-- DL envelopes -->
<div class="piece env env-b">
  <svg class="art" viewBox="0 0 330 125" preserveAspectRatio="none" aria-hidden="true">
    <path d="M0 0 H34 C26 14 14 26 0 34 Z" fill="url(#blueGrad)"/>
    <path d="M0 112 C110 106 220 118 330 104 V125 H0 Z" fill="url(#blueGrad)"/>
  </svg>
  <div class="brand"><span class="brand-dot"></span><span class="brand-name">Korvane Technologies</span></div>
  <div class="return-address">120 Meridian Way, Suite 4, Ottawa</div>
</div>

<div class="piece env env-c">
  <svg class="art" viewBox="0 0 330 125" preserveAspectRatio="none" aria-hidden="true">
    <path d="M0 0 H34 C26 14 14 26 0 34 Z" fill="url(#blueGrad)"/>
    <path d="M0 112 C110 106 220 118 330 104 V125 H0 Z" fill="url(#blueGrad)"/>
  </svg>
  <div class="brand"><span class="brand-dot"></span><span class="brand-name">Korvane Technologies</span></div>
  <div class="return-address">120 Meridian Way, Suite 4, Ottawa</div>
  <div class="window"></div>
</div>
</body>
</html>
```